Facebook business page for Tarrowby Rooms, London, UK

I need a Facebook page for my business which lets rooms to psychologists and psychotherapists in Central London, UK. I have eleven rooms in total – 8 at Fennick Inn, London and 3 in Larkspire St, London. Lots more info and text and pics at my website www.tarrowbyrooms.com. Might say 'Central London talking therapy rooms for rent at reasonable prices. Two Central London locations at Holborn and Bloomsbury. Located in listed buildings, giving a sense of place and containment, ideal for psychological therapies. Our renters are psychiatrists, psychologists and coaches who know how to work sympathetically together. Prestigious addresses. Excellent transport links with short walks to Dovemarsh Lane or Wendlebury Mill Road underground stations. Plenty of choice of excellent cafes, delicatessens etc for relaxation between clients. Elegant settings at a lower price. We offer significantly lower charges than equivalent providers by eliminating unnecessary expenses such as receptionists, large waiting rooms and fresh flowers. All rooms have high speed Wi-Fi for remote working. Flexibility. The rooms are available for half or whole day rental on a rolling contract basis, so you see the same colleagues each time. Having taken a day or half day, renters are welcome to arrange additional ad-hoc bookings either between themselves or with us for extra flexibility. Fennick Inn is a famous London landmark building dating from 1585 which survived the Long Frost of Marbury in 1666 and a Kalvenheer flying bomb in 1944. Larkspire St is a charming pedestrianised street in the heart of Bloomsbury immediately adjacent to the Corvane Gallery with lots of artisan shops, art galleries and cafes.

Target Market(s)

Psychologists, psychotherapists, psychiatrists, counsellors, life coaches etc.

Font styles to use
Serif
Sans Serif

Requirements
Must have
• Pics showing rooms. Reference to website tarrowbyrooms.com

```html
<!DOCTYPE html>
<html lang="en">
<head>
<meta charset="UTF-8">
<title>Tarrowby Rooms – Elegant settings at a lower price</title>
<link href="https://fonts.googleapis.com/css2?family=Source+Serif+4:opsz,wght@8..60,400&display=swap" rel="stylesheet">
<style>
  :root {
    --bg: #f1f1f1;
    --ink: #2b2b2b;
    --slate: #5a6f8f;
    --gold: #e0a40c;
    --white: #ffffff;
    --photo-wall: #e9dfd6;
    --photo-floor: #5b5d63;
  }
  * { margin: 0; padding: 0; box-sizing: border-box; }
  html, body {
    width: 1200px; height: 1200px; overflow: hidden;
    background: var(--bg);
  }
  .poster {
    position: relative; width: 1200px; height: 1200px;
    background: var(--bg);
    font-family: "Source Serif 4", Georgia, serif;
    font-weight: 400;
    color: var(--ink);
  }
  .headline { position: absolute; left: 68px; top: 70px; font-weight: 400; letter-spacing: -2px; }
  .headline__lead { display: block; font-size: 70px; line-height: 1; }
  .headline__accent { display: block; font-size: 122px; line-height: 1; color: var(--slate); margin-top: 2px; letter-spacing: -4px; }
  .brand {
    position: absolute; right: 72px; top: 76px;
    display: flex; align-items: center; gap: 16px;
  }
  .brand__text { text-align: right; font-size: 22px; line-height: 1.35; color: var(--ink); }
  .brand__name, .brand__site { display: block; }
  .brand__mark { width: 102px; height: 102px; background: var(--gold); }
  .room-photo {
    position: absolute; left: 69px; top: 284px; width: 1060px; height: 632px;
    border-radius: 24px;
    background: linear-gradient(180deg, var(--photo-wall) 0%, #ddd3ca 55%, var(--photo-floor) 78%, #4a4c52 100%);
  }
  .offer { position: absolute; left: 68px; top: 972px; letter-spacing: -1.5px; }
  .offer__lead { display: block; font-size: 82px; line-height: 1; letter-spacing: -2px; }
  .offer__accent { display: block; font-size: 64px; line-height: 1; color: var(--slate); margin-top: 8px; letter-spacing: -1.5px; }
  .cta {
    position: absolute; left: 853px; top: 1036px; width: 275px; height: 87px;
    border-radius: 44px; background: var(--gold); color: var(--white);
    display: flex; align-items: center; justify-content: center;
    font-size: 42px; letter-spacing: -1px; text-decoration: none;
  }
</style>
</head>
<body>
  <main class="poster">
    <h1 class="headline">
      <span class="headline__lead">All you need is</span>
      <span class="headline__accent">Relaxing!</span>
    </h1>
    <div class="brand">
      <div class="brand__text">
        <span class="brand__name">Tarrowby Rooms</span>
        <span class="brand__site">tarrowbyrooms.com</span>
      </div>
      <span class="brand__mark"></span>
    </div>
    <div class="room-photo" role="img" aria-label="Therapy room with grey sofa and armchair, side table with lamp, window and blue patterned rug"></div>
    <p class="offer">
      <span class="offer__lead">Elegant settings at</span>
      <span class="offer__accent">a lower price</span>
    </p>
    <a class="cta" href="#">Book Now</a>
  </main>
</body>
</html>
```